Grain Clear Kitchen Web Design

We are looking for designs for a homepage for a Grain Clear, health food website.

We are looking for the site to be a shop, as well as a resource/information source for users. We will also look to incorporate recipes, blogs, forums and potentially some other useful information.

We want to ensure that the website is user-friendly, does not have a corporate feel, but is still classy.

We want to have high quality photographic images in the background, with text in the foreground - but these things will need to compliment each other well. e.g recipe of the week integrated onto the background photo and the 'shop' in the foreground.

We have seen a site that we quite like and although we like the design, we do not want to completely emulate this. However, it is a useful starting point for designers and perhaps some inspiration www.brightpantryhall.example

We already have a logo - see attached - which will need to be fully integrated into the design.

We do want a colourful design, but mainly in terms of the images rather than the graphics.
Updates

Please note:

We are pleased with the designs to date, for the most part. We would like you all to note, however, that we are much preferring the lighter designs - ones that make the sites feel brighter - rather than those which are darker in appearance.

We would also like to see less space allocated to the main image, within the context of the site as a whole.

Thanks.

We have eliminated those which we feel are not what we are looking for. We are still keen to see some more designs and are still looking for something unique. There are some good things in all of the designs that we have not eliminated, however we still feel there is room for more inspiration.

Thanks.

Target Market(s)

Our audience are body conscience people looking for health food products. They are also those who are potentially looking for a new lifestyle/life cha

Industry/Entity Type

Health

Requirements
Must have
• Our logo - attached, can provide variations in due course.

Navigational features as per mock up attached.

Social network integration.

NB: we only need one (home) page for this.

```html
<!DOCTYPE html>
<html lang="en">
<head>
<meta charset="utf-8">
<title>Grain Clear Kitchen</title>
<link rel="stylesheet" href="https://fonts.googleapis.com/css2?family=Open+Sans:wght@300;400;600&display=swap">
<style>
:root{
  --ink:#3a3a3a;
  --soft:#5a5a5a;
  --dark:#2e2e2e;
  --charcoal:#3b3b3b;
  --panel:#ffffff;
  --panel-tint:#efe9e8;
  --button:#e9e7e6;
  --grey-btn:#9a9a9a;
  --link:#1e8fc6;
  --accent:#4db848;
  --footer:#232323;
  --footer-line:#3a3a3a;
  --footer-text:#dcdcdc;
}
*{box-sizing:border-box;margin:0;padding:0}
html,body{width:1200px;height:976px;overflow:hidden}
body{position:relative;font-family:"Open Sans",sans-serif;color:var(--ink);background:#fff}
.abs{position:absolute}
.hero-photo{left:0;top:0;width:1200px;height:741px;
  background:
   radial-gradient(ellipse 260px 180px at 120px 240px,#e0301d 0%,rgba(224,48,29,0) 70%),
   radial-gradient(ellipse 300px 200px at 520px 160px,#f2c31d 0%,rgba(242,195,29,0) 70%),
   radial-gradient(ellipse 260px 200px at 860px 220px,#e33a22 0%,rgba(227,58,34,0) 70%),
   radial-gradient(ellipse 240px 200px at 1110px 150px,#f0a623 0%,rgba(240,166,35,0) 70%),
   radial-gradient(ellipse 380px 200px at 300px 460px,#c9402a 0%,rgba(201,64,42,0) 70%),
   radial-gradient(ellipse 300px 200px at 960px 460px,#d8351f 0%,rgba(216,53,31,0) 70%),
   linear-gradient(180deg,#f7b45a 0%,#ef7a3a 45%,#f3dcd0 80%,#ffffff 100%)}
.header-band{left:0;top:0;width:1200px;height:90px;background:rgba(255,255,255,.9);border-bottom:1px solid #d8d0cc}
.brand{left:218px;top:0;width:142px;height:124px;background:#f4f1ef;display:flex;flex-direction:column;align-items:center;justify-content:center;gap:6px;box-shadow:0 2px 6px rgba(0,0,0,.2)}
.brand-dot{width:26px;height:26px;border-radius:50%;background:var(--dark)}
.brand-name{font-size:15px;font-weight:600;color:var(--dark);text-align:center;line-height:1.15}
.basket{left:547px;top:15px;width:182px;height:27px;display:flex;font-size:12px}
.basket-count{flex:1;border:1px solid var(--dark);background:#fff;padding-left:16px;line-height:25px}
.basket-label{width:78px;background:#3d2d2e;color:#fff;text-align:center;line-height:27px;font-size:13px}
.btn-grey{top:15px;height:27px;background:var(--grey-btn);color:#fff;font-size:14px;text-align:center;line-height:27px;outline:1px solid #c8c8c8;outline-offset:1px}
.login{left:737px;width:71px}
.register{left:812px;width:72px;font-size:13px}
.search{left:891px;top:15px;width:165px;height:27px;display:flex}
.search-field{flex:1;border:1px solid var(--dark);background:#fff;font-size:11px;font-style:italic;padding-left:12px;line-height:25px;color:var(--soft)}
.search-btn{width:33px;background:var(--charcoal);display:flex;align-items:center;justify-content:center}
.main-nav{right:151px;top:59px;display:flex;font-size:13px;color:var(--ink)}
.main-nav span{padding:0 10px;border-left:1px solid #aaa;line-height:1}
.main-nav span:first-child{border-left:none}
.main-nav span:last-child{padding-right:0}
.welcome{left:412px;top:127px;width:596px;height:37px;background:#f2f0ef;font-size:15px;text-align:center;line-height:37px;color:var(--ink)}
.fold-l{left:412px;top:116px;width:35px;height:11px;background:#b8b8b8;clip-path:polygon(0 100%,100% 0,100% 100%)}
.fold-r{left:973px;top:164px;width:35px;height:12px;background:#b8b8b8;clip-path:polygon(0 0,100% 0,0 100%)}
.intro{left:163px;top:202px;width:207px;height:136px;background:rgba(255,255,255,.93);border:2px solid #fff}
.intro h2{background:var(--charcoal);color:#fff;font-weight:300;font-size:19px;height:34px;line-height:34px;text-align:center}
.intro p{font-size:10.5px;line-height:16px;padding:11px 12px;color:var(--soft)}
.side-btn{left:162px;width:208px;height:33px;background:var(--button);border:2px solid #fff;font-size:17px;font-weight:300;padding-left:18px;line-height:29px;color:var(--ink)}
.card{background:rgba(255,255,255,.95);border:2px solid #f3f3f3}
.card-head{height:36px;background:var(--panel-tint);font-size:19px;font-weight:300;line-height:36px;position:relative}
.card-head svg{position:absolute;right:8px;top:8px}
.recipe{left:383px;top:203px;width:424px;height:248px}
.recipe .card-head{padding-left:22px}
.photo-main{left:12px;top:49px;width:209px;height:133px;background:linear-gradient(160deg,#efe6d6,#e9d9b8 50%,#c64a3c 75%,#6b4a3a)}
.thumb{top:189px;width:64px;height:45px}
.t1{left:12px;background:linear-gradient(#5a3728,#2e1c16)}
.t2{left:84px;background:linear-gradient(#e7a8b6,#cfe3d4)}
.t3{left:156px;background:linear-gradient(#6a4a2e,#d8b88a)}
.recipe-title{left:235px;top:44px;font-size:18px;font-weight:300}
.recipe-text{left:235px;top:75px;width:182px;font-size:10.5px;line-height:16px;color:var(--soft)}
.recipe-text p+p{margin-top:14px}
.more{color:var(--link)}
.recipe-cta{left:235px;top:214px;width:194px;height:24px;background:var(--charcoal);color:#fff;font-size:13px;padding-left:13px;line-height:24px}
.recipe-cta svg{position:absolute;right:10px;top:6px}
.posts{left:822px;top:203px;width:242px;height:248px}
.posts .card-head{text-align:center}
.post-date{left:9px;top:44px;color:var(--link);font-size:25px;font-weight:300;line-height:1}
.post-month{left:11px;top:72px;color:var(--link);font-size:8px}
.post-title{left:53px;top:58px;font-size:17px;font-weight:300}
.post-text{left:9px;top:92px;width:226px;font-size:10.5px;line-height:16px;color:var(--soft)}
.post-tags{left:9px;top:183px;font-size:10px;color:var(--soft)}
.post-tags a{color:var(--link);text-decoration:none}
.post-author{right:8px;top:183px;font-size:10.5px;font-weight:600}
.post-foot{left:3px;top:211px;width:234px;height:32px;background:var(--button);font-size:13px}
.post-foot .blog{position:absolute;left:0;top:0;width:76px;height:32px;background:#d6d3d2;text-align:center;line-height:32px}
.post-foot .all{position:absolute;right:40px;top:0;line-height:32px}
.corner{position:absolute;right:0;bottom:0;width:34px;height:34px;background:var(--charcoal);clip-path:polygon(100% 0,100% 100%,0 100%)}
.corner svg{position:absolute;right:4px;bottom:4px}
.product{top:476px;width:167px;height:213px}
.product .name{height:35px;background:var(--panel-tint);text-align:center;font-size:14.5px;font-weight:300;line-height:36px}
.product .shot{height:142px}
.price-bar{position:absolute;left:2px;bottom:2px;width:163px;height:32px;background:var(--button);font-size:13px}
.price{position:absolute;left:0;top:0;width:76px;height:32px;background:#dedcdb;font-size:16px;font-weight:300;padding-left:10px;line-height:32px}
.add{position:absolute;left:93px;top:0;line-height:32px}
.plus{position:absolute;right:0;bottom:0;width:30px;height:30px;background:var(--charcoal);clip-path:polygon(100% 0,100% 100%,0 100%);color:#fff;font-size:11px;text-align:right;padding-right:5px;line-height:40px}
.p1{left:162px}.p2{left:347px}.p3{left:532px}.p4{left:716px}.p5{left:900px}
.s-oat{background:radial-gradient(circle at 50% 55%,#f2b73a 0 30%,#fff 60%)}
.s-pretzel{background:radial-gradient(circle at 50% 50%,#8a3c1c 0 25%,#f08a1e 45%,#f4a12e)}
.s-bread{background:linear-gradient(90deg,#b98a4c,#e6c79a 25%,#8b6a3f 50%,#e6c79a 75%,#b98a4c)}
.s-pasta{background:linear-gradient(180deg,#c23426 0%,#1f3a2a 40%,#f2c42a 85%)}
.footer{left:0;top:741px;width:1200px;height:199px;background:var(--footer);color:var(--footer-text)}
.footer-top{position:absolute;left:0;top:0;width:1200px;height:37px;background:#1c1c1c}
.f-head{top:12px;font-size:15px;font-weight:600;color:#fff}
.f-list{top:44px;width:206px;list-style:none;font-size:11px}
.f-list li{height:27px;line-height:27px;border-bottom:1px solid var(--footer-line);padding-left:15px}
.f-news{left:390px;top:50px;width:178px;font-size:11px;line-height:18px;color:#f2f2f2}
.f-form{left:390px;top:126px;width:192px;height:34px;display:flex;border:1px solid #fff}
.f-form .field{flex:1;background:#fff;color:#444;font-size:11.5px;font-style:italic;padding-left:13px;line-height:32px}
.f-form .go{width:34px;background:var(--accent);display:flex;align-items:center;justify-content:center}
.f-contact{left:849px;top:44px;font-size:11px;line-height:18px;color:#f2f2f2}
.f-contact .mail{color:var(--accent)}
.social{left:847px;top:143px;display:flex;gap:4px}
.social span{width:27px;height:25px;background:#5a5a5a;border-radius:2px}
.copyright{left:0;top:940px;width:1200px;height:36px;background:#1a1a1a;color:#ddd;font-size:9px;padding-left:264px;line-height:34px}
</style>
</head>
<body>
<div class="abs hero-photo" role="img" aria-label="Blurred background photograph of fresh strawberries and fruit"></div>
<header>
  <div class="abs header-band"></div>
  <div class="abs brand"><span class="brand-dot"></span><span class="brand-name">Grain Clear<br>Kitchen</span></div>
  <div class="abs basket"><span class="basket-count">0 Item(s) in</span><span class="basket-label">Basket</span></div>
  <div class="abs btn-grey login">Login</div>
  <div class="abs btn-grey register">Register</div>
  <div class="abs search"><span class="search-field">Product search.....</span><span class="search-btn"><svg width="16" height="16" viewBox="0 0 16 16"><circle cx="6.5" cy="6.5" r="5" fill="none" stroke="#fff" stroke-width="2"/><line x1="10.2" y1="10.2" x2="15" y2="15" stroke="#fff" stroke-width="2.2"/></svg></span></div>
  <nav class="abs main-nav"><span>Shop</span><span>Our Story</span><span>Hints &amp; tips</span><span>Recipes</span><span>Blog</span><span>Contact</span></nav>
</header>

<div class="abs fold-l"></div>
<div class="abs welcome">Welcome to Grain Clear&nbsp; - &nbsp;Kitchen&nbsp; - &nbsp;The one stop shop for everthing Grain Clear</div>
<div class="abs fold-r"></div>

<section class="abs intro">
  <h2>Grain Clear&nbsp; - &nbsp;Kitchen</h2>
  <p>Ut scelerisque diam. Donec pulvinar ultricies sem, vel dapibus eros Maecenas auctor.Ut scelerisque diam. Donec pulvinar ultricies sem, vel dapibus eros Maecenas auctor.</p>
</section>
<div class="abs side-btn" style="top:342px">Latest Posts</div>
<div class="abs side-btn" style="top:380px">View all Recipes</div>
<div class="abs side-btn" style="top:419px">Go to the Shop</div>

<section class="abs card recipe">
  <div class="card-head">New York baked cheesecake<svg width="13" height="11" viewBox="0 0 13 11"><path d="M1 4v6h9V7" fill="none" stroke="#555" stroke-width="1.5"/><path d="M5 7c1-3 3-4 6-4M9 1l3 2-3 2" fill="none" stroke="#555" stroke-width="1.5"/></svg></div>
  <div class="abs photo-main" role="img" aria-label="Photo of a strawberry topped baked cheesecake"></div>
  <div class="abs thumb t1" role="img" aria-label="Photo of a chocolate layer cake"></div>
  <div class="abs thumb t2" role="img" aria-label="Photo of pastel sweets"></div>
  <div class="abs thumb t3" role="img" aria-label="Photo of chocolate chip muffins"></div>
  <div class="abs recipe-title">Ut scelerisque diam.</div>
  <div class="abs recipe-text"><p>Donec pulvinar ultricies sem, vel dapibus eros Maecenas auctor.Ut scelerisque diam. Donec pulvinar ultricies sem, vel dapibus eros Maecenas auctor.</p><p>Ut scelerisque diam. Donec pulvinar ultricies sem, vel dapibus <span class="more">more...</span></p></div>
  <div class="abs recipe-cta">Full&nbsp; Recipe<svg width="11" height="11" viewBox="0 0 11 11"><circle cx="4.5" cy="4.5" r="3.3" fill="none" stroke="#fff" stroke-width="1.4"/><line x1="7" y1="7" x2="10" y2="10" stroke="#fff" stroke-width="1.6"/></svg></div>
</section>

<section class="abs card posts">
  <div class="card-head">Latest Posts<svg width="13" height="11" viewBox="0 0 13 11"><path d="M1 4v6h9V7" fill="none" stroke="#555" stroke-width="1.5"/><path d="M5 7c1-3 3-4 6-4M9 1l3 2-3 2" fill="none" stroke="#555" stroke-width="1.5"/></svg></div>
  <div class="abs post-date">04</div>
  <div class="abs post-month">Jan 11</div>
  <div class="abs post-title">Donec pulvinar ultricies</div>
  <div class="abs post-text">vel dapibus eros Maecenas auctor quam sit amet ante tristique sodales.vel dapibus eros Maecenas auctor quam sit amet ante. tristique sodales.vel dapibus eros Maecenas auctor quam sit amet ante tristique <span class="more">more...</span></div>
  <div class="abs post-tags">Tags: <a>Latest new</a>, <a>Grain Clear</a></div>
  <div class="abs post-author">- Amy Reed</div>
  <div class="abs post-foot"><span class="blog">Blog</span><span class="all">View all posts</span><span class="corner"><svg width="12" height="12" viewBox="0 0 12 12"><circle cx="5" cy="5" r="3.6" fill="none" stroke="#fff" stroke-width="1.4"/><line x1="7.6" y1="7.6" x2="11" y2="11" stroke="#fff" stroke-width="1.6"/></svg></span></div>
</section>

<section class="abs card product p1"><div class="name">Product Name</div><div class="shot s-oat" role="img" aria-label="Product photo of a box of oatcakes"></div><div class="price-bar"><span class="price">£ 0.50</span><span class="add">Add to</span><span class="plus">+</span></div></section>
<section class="abs card product p2"><div class="name">Product Name</div><div class="shot s-pretzel" role="img" aria-label="Product photo of a bag of pretzels"></div><div class="price-bar"><span class="price">£ 2.50</span><span class="add">Add to</span><span class="plus">+</span></div></section>
<section class="abs card product p3"><div class="name">Product Name</div><div class="shot s-bread" role="img" aria-label="Product photo of two sliced bread loaves"></div><div class="price-bar"><span class="price">£ 5.50</span><span class="add">Add to</span><span class="plus">+</span></div></section>
<section class="abs card product p4"><div class="name">Product Name</div><div class="shot s-pasta" role="img" aria-label="Product photo of a pasta pack with tomatoes"></div><div class="price-bar"><span class="price">£ 4.98</span><span class="add">Add to</span><span class="plus">+</span></div></section>
<section class="abs card product p5"><div class="name">Product Name</div><div class="shot s-bread" role="img" aria-label="Product photo of two sliced bread loaves"></div><div class="price-bar"><span class="price">£ 2.50</span><span class="add">Add to</span><span class="plus">+</span></div></section>

<footer class="abs footer">
  <div class="footer-top"></div>
  <div class="abs f-head" style="left:169px">Useful links</div>
  <ul class="abs f-list" style="left:162px"><li>Contact us</li><li>FAQs</li><li>Site Map</li><li>Privacy Policy</li></ul>
  <div class="abs f-head" style="left:390px;top:10px">Newsletter sign up</div>
  <p class="abs f-news">To keep upto date with the latest news and information about our services please fill out your Email address below:</p>
  <div class="abs f-form"><span class="field">email address</span><span class="go"><svg width="18" height="18" viewBox="0 0 18 18"><circle cx="9" cy="9" r="7.5" fill="none" stroke="#fff" stroke-width="1.5"/><path d="M5 9h7M9 5.5 12.5 9 9 12.5" fill="none" stroke="#fff" stroke-width="1.6"/></svg></span></div>
  <div class="abs f-head" style="left:620px">Your account</div>
  <ul class="abs f-list" style="left:616px"><li>Create Account</li><li>Sign In</li><li>Shopping basket</li><li>Store Locations</li><li>Customer Service</li></ul>
  <div class="abs f-head" style="left:842px">Stay in touch</div>
  <div class="abs f-contact">27 Mill Row,<br>Fenwick,<br>Eastshire , EF4 2QL<br>+44(0) 1632 960 418<br><span class="mail">info@grainclearkitchen.example</span></div>
  <div class="abs social" aria-label="Social links"><span></span><span></span><span></span><span></span></div>
</footer>
<div class="abs copyright">Copyright © 2013 Studio Linden. Use of this website constitutes acceptance of our User Agreement and Privacy Policy.</div>
</body>
</html>
```